Web Page for Elearning project

SUMMARY OF REQUIREMENT
The requirement is to provide the graphic design for an eLearning project. I need the design elements for a main page layout which I can recreate in an eLearning authoring program (Quillet) using the graphic design you provide.

SUMMARY OF SITE PAGES
The web site has 11 sections with pages within each section. The user will navigate through all pages by clicking NEXT or by jumping to a page using either an index or table of contents (according to your design).

The sections are:
- Introduction
- DWT Cemeteries
- Fernhallow*
- Plain of Wrens (Catholic)*
- East Vales (Catholic)*
- Ashbury (Catholic)*
- Tallis Brook (Catholic)*
- Plain of Wrens (Presbyterian)*
- Pell Ridge*
- Summary
- Quiz

The sections with a "*" contain consistent pages - which I imagine could be accessed by clicking on a tab or button. I would need you to supply the graphics to be able to set them up in my elearning program. The pages are:
- History
- Map
- Contact
- Directions
- Services
- Sections

ONCE THE DESIGN IS ACCEPTED...
Ultimately I need the background graphics so I can implement the design in my elearning authoring program What else do you need to know?

SEE ATTACHED PDF FOR MORE DETAILS AND EXAMPLES OF WHAT I AM CURRENTLY WORKING WITH
Updates

Reason: Australia now has public holidays for the next 5 days.  Everyone back at work on 27-28 April.

Target Market(s)

The users are mostly middle-aged women who only have basic computer skills... needs to be easy to navigate.

Industry/Entity Type

Graphic Design

Requirements
Must have
• Light, fun but professional. Its training...should have a light/easy feel about it.

Must be easy to look at. The design should support the overall navigation/structure.
Nice to have
• easy to look at, light.
Should not have
• Should not use serif fonts.
I don't think we'd go for bold lime green or any really zany colours.

```html
<!DOCTYPE html>
<html lang="en">
<head>
<meta charset="utf-8">
<title>DWT Cemeteries Module – Fernhallow</title>
<link rel="stylesheet" href="https://fonts.googleapis.com/css2?family=Open+Sans:wght@400;600&display=swap">
<style>
:root{
  --page:#ffffff;
  --ink:#222222;
  --link:#1f6fe0;
  --navy:#1b3d7a;
  --side-top:#9ccaf4;
  --side-bottom:#4a72bd;
  --side-text:#ffffff;
  --tab-top:#8fbaf2;
  --tab-bottom:#3f6fc7;
  --btn-top:#c9413c;
  --btn-bottom:#9e1d1b;
  --shadow:#444a55;
  --frame:#9a9a9a;
  --box:#4d6aa8;
  --grey-logo:#8ba0b3;
  --figure:#37c3e3;
}
*{box-sizing:border-box;margin:0;padding:0}
html,body{width:1200px;height:891px;overflow:hidden;background:var(--page)}
body{font-family:"Open Sans",Verdana,sans-serif;color:var(--ink)}
.stage{position:relative;width:1200px;height:891px}

.brand{position:absolute;left:40px;top:80px;display:flex;align-items:center;gap:12px;
  font-size:34px;font-weight:600;color:var(--navy);letter-spacing:1px}
.brand-dot{width:22px;height:22px;border-radius:50%;background:var(--navy)}

.section-tab{position:absolute;left:311px;top:51px;width:240px;height:40px;
  background:linear-gradient(var(--tab-top),var(--tab-bottom));
  box-shadow:4px 4px 0 var(--shadow);color:#fff;font-size:22px;
  padding:5px 0 0 16px}

.nav-btn{position:absolute;top:48px;height:46px;
  background:linear-gradient(var(--btn-top),var(--btn-bottom));
  box-shadow:4px 4px 0 var(--shadow);color:#fff;font-size:26px;
  display:flex;align-items:center;justify-content:center}
.nav-back{left:859px;width:127px}
.nav-next{left:1004px;width:127px}
.nav-close{left:1149px;width:44px}

.index{position:absolute;left:9px;top:215px;width:290px;height:483px;
  background:linear-gradient(var(--side-top),var(--side-bottom));
  box-shadow:5px 5px 0 var(--shadow);list-style:none;padding-top:14px}
.index li{height:41.7px;display:flex;align-items:center;gap:12px;
  padding-left:9px;color:var(--side-text);font-size:16.5px;letter-spacing:.3px}
.check{width:20px;height:20px;background:var(--box);border:1px solid #fff;
  flex:none;position:relative}
.check svg{position:absolute;left:1px;top:0}

.panel{position:absolute;left:311px;top:115px;width:885px;height:590px;
  border:1px solid var(--frame);background:#fff}
.bubbles{position:absolute;left:0;top:0}
.bubble-main{position:absolute;left:79px;top:88px;width:470px;font-size:15px;line-height:18.75px}
.bubble-main p{margin-bottom:18.75px}
.bubble-main a,.bubble-side a{color:var(--link);text-decoration:none}
.bubble-side{position:absolute;left:689px;top:148px;width:165px;font-size:15px;line-height:19px}
.figure{position:absolute;left:590px;top:273px;width:256px;height:300px;
  border-radius:40px 40px 12px 12px;
  background:linear-gradient(160deg,#7fdcef,var(--figure))}

.footer-links{position:absolute;left:12px;top:714px;list-style:none;font-size:15.5px;line-height:23.5px}
.footer-links a{color:var(--ink)}

.tools{position:absolute;left:396px;top:731px}
.tool{position:absolute;top:0;width:98px;height:90px;
  background:linear-gradient(var(--btn-top),var(--btn-bottom));
  box-shadow:4px 4px 0 var(--shadow);color:#fff;font-size:15.5px;
  display:flex;flex-direction:column;align-items:center;justify-content:flex-end;padding-bottom:6px;gap:4px}
.tool svg{width:52px;height:52px}

.module-name{position:absolute;left:10px;top:853px;display:flex;align-items:center;gap:12px;
  font-size:22px;font-weight:600;color:var(--grey-logo)}
.module-name .brand-dot{width:18px;height:18px;background:var(--grey-logo)}
.page-count{position:absolute;left:1062px;top:856px;font-size:20px;color:#333}
</style>
</head>
<body>
<div class="stage">

  <div class="brand"><span class="brand-dot"></span>DWT</div>

  <div class="section-tab">Fernhallow</div>
  <div class="nav-btn nav-back">Back</div>
  <div class="nav-btn nav-next">Next</div>
  <div class="nav-btn nav-close">X</div>

  <ul class="index">
    <li><span class="check"></span>Introduction</li>
    <li><span class="check"></span>DWT Cemeteries</li>
    <li><span class="check"><svg width="18" height="18" viewBox="0 0 18 18"><path d="M3 9l4 4 8-10" fill="none" stroke="#3fc0ef" stroke-width="2.5"/></svg></span>Fernhallow</li>
    <li><span class="check"></span>Plain of Wrens (Catholic)</li>
    <li><span class="check"></span>East Vales (Catholic)</li>
    <li><span class="check"></span>Ashbury (Catholic)</li>
    <li><span class="check"></span>Tallis Brook (Catholic)</li>
    <li><span class="check"></span>Plain of Wrens (Presbyterian)</li>
    <li><span class="check"></span>Pell Ridge</li>
    <li><span class="check"></span>Summary</li>
    <li><span class="check"></span>Quick Quiz</li>
  </ul>

  <div class="panel">
    <svg class="bubbles" width="885" height="590" viewBox="0 0 885 590">
      <path d="M300 398 L455 482 L415 375 A280 197 0 1 0 300 398 Z" fill="#fff" stroke="#000" stroke-width="3" stroke-linejoin="miter"/>
      <path d="M740 239 L755 262 L770 240 A109.5 59.5 0 1 0 740 239 Z" fill="#fff" stroke="#000" stroke-width="3"/>
    </svg>
    <div class="bubble-main">
      <p>The first time you read this module you might want to read all the way through. Just keep clicking the <a href="#">NEXT</a> button to read every page.</p>
      <p>If you want to find information about a cemetary, jump to the cemetary page using the index on the left.</p>
      <p>Read the module as many times as you want, if you have any questions ask your supervisor.</p>
      <p>At the end of the module you can complet a short quiz. It’s fun so have a go to see how much you have learnt.</p>
    </div>
    <div class="bubble-side">Click <a href="#">HERE</a> and I’ll show you the index.</div>
    <div class="figure" role="img" aria-label="Cheerful cartoon guide in a tie giving a thumbs up"></div>
  </div>

  <ul class="footer-links">
    <li><a href="#">Home</a></li>
    <li><a href="#">Help</a></li>
    <li><a href="#">Resources</a></li>
    <li><a href="#">Links</a></li>
  </ul>

  <div class="tools">
    <div class="tool" style="left:0">
      <svg viewBox="0 0 52 52"><path d="M4 12q11-4 21 2v30q-10-6-21-2zM48 12q-11-4-21 2v30q10-6 21-2z" fill="#fff"/></svg>History</div>
    <div class="tool" style="left:126px">
      <svg viewBox="0 0 52 52"><rect x="4" y="4" width="44" height="44" fill="#f1ece4"/><circle cx="22" cy="21" r="10" fill="none" stroke="#222" stroke-width="3"/><path d="M29 28l12 12" stroke="#222" stroke-width="5"/></svg>Map</div>
    <div class="tool" style="left:255px">
      <svg viewBox="0 0 52 52"><path d="M6 20q20-14 40 0l-3 6-8-3v-4q-9-3-18 0v4l-8 3z" fill="#fff"/><path d="M14 26h24l6 16H8z" fill="#fff"/><circle cx="26" cy="34" r="5" fill="#b52a27"/></svg>Contact</div>
    <div class="tool" style="left:383px">
      <svg viewBox="0 0 52 52"><rect x="23" y="4" width="5" height="44" fill="#fff"/><path d="M8 8h32l6 5-6 5H8zM12 22h32v10H12l-6-5z" fill="#fff"/></svg>Directions</div>
    <div class="tool" style="left:513px">
      <svg viewBox="0 0 52 52"><path d="M25 2h2v6h4v2h-4v4l8 10v24H15V24l8-10v-4h-4V8h4z" fill="#fff"/><path d="M6 32l9-6v22H6zM46 32l-9-6v22h9z" fill="#fff"/><rect x="23" y="36" width="6" height="12" fill="#b52a27"/></svg>Services</div>
    <div class="tool" style="left:644px">
      <svg viewBox="0 0 52 52"><path d="M21 4h10v12h13v10H31v24H21V26H8V16h13z" fill="#fff"/></svg>Sections</div>
  </div>

  <div class="module-name"><span class="brand-dot"></span>DWT CEMETERIES MODULE</div>
  <div class="page-count">Page: 1 of 7</div>

</div>
</body>
</html>
```